Infographic from a blog post about Reliability Centred Maintenance (RCM)

I need someone to convert a detailed blog post into an Infographic. The post is here: https://www.gearmontlabs.com/reliability-centered-maintenance-principles/

The infographic should include:
(1) the history of RCM, probably best done by using the 1st, 2nd and 3rd generation of maintenance concepts as discussed in the article. For the 3rd generation includesome of the metrics that show the difference RCM made e.g. the comparison between the maintenance of a QX-7 versus that of the 583-240

(2) All the 9 principles that are mentioned in the article with a large part of the infographic dedicated to Principle #2 with the failure patterns and distributions

For the infographic make sure it fits with the design & branding of the overall site www.gearmontlabs.com

Industry/Entity Type

Industrial

Font styles to use
Other font styles liked:
• roboto condensed bold for titles, raleway for text

Colors
0292cd
333333
ffc214

Requirements
Must have
• The infographic must include:
• (1) the history of RCM and some of the metrics that show the difference RCM made e.g. the comparison between the maintenance of a QX-7 versus that of the 583-240
• (2) All the 9 principles that are mentioned in the article with a large part of the infographic dedicated to Principle #2 with the failure patterns and distributions
• Use following main colours:
• #3C3C3C
• #0187AC
• Use the following colors for highlights:
• #079F6D
• #B91449
• #FFC000
Nice to have
• For the history section use some imagery along these lines:
• 1st generation of maintenance = industrial revolution so steam train, steam equipment
• 2nd generation of maintenance = from world war 2, maybe show a tank
• 3rd generation of maintenance = developed by aviation so show a picture of a 583-240 airplane

```html
<!DOCTYPE html>
<html lang="en">
<head>
<meta charset="utf-8">
<title>Reliability Centred Maintenance (RCM)</title>
<link rel="stylesheet" href="https://fonts.googleapis.com/css2?family=Roboto+Condensed:wght@700&family=Raleway:wght@300;400;600;700&display=swap">
<style>
  :root {
    --ink: #3c3c3c;
    --blue: #0187ac;
    --green: #079f6d;
    --crimson: #b91449;
    --gold: #ffc000;
    --paper: #ffffff;
    --card: #f6f7f7;
    --text: #555555;
    --strong: #1f1f1f;
    --maroon: #8a1b45;
    --teal: #125a73;
  }
  * { margin: 0; padding: 0; box-sizing: border-box; }
  html, body { width: 929px; height: 1200px; overflow: hidden; background: var(--paper); }
  .canvas { position: relative; width: 929px; height: 1200px; overflow: hidden; font-family: "Raleway", sans-serif; color: var(--text); }

  .masthead { position: absolute; left: 0; top: 0; width: 929px; height: 146px; background: var(--ink); }
  .masthead h1 { position: absolute; left: 18px; top: 44px; font-family: "Roboto Condensed", sans-serif; font-weight: 700; font-size: 53px; line-height: 1; color: #fff; white-space: nowrap; }

  .side-rail { position: absolute; right: 0; top: 196px; }

  .section-title { position: absolute; left: 138px; font-family: "Roboto Condensed", sans-serif; font-weight: 700; font-size: 64px; line-height: 1; color: var(--ink); }
  .section-rule { position: absolute; left: 111px; width: 699px; height: 2px; background: var(--blue); }

  .gen-card { position: absolute; top: 306px; height: 329px; background: var(--paper); border: 1px solid #d6d6d6; }
  .gen-card__head { height: 48px; color: #fff; font-size: 24px; font-weight: 400; display: flex; align-items: center; justify-content: center; }
  .gen-card__body { background: var(--card); text-align: center; font-size: 13.6px; line-height: 17.3px; padding-top: 16px; }
  .gen-card__body b { font-weight: 600; color: var(--strong); }
  .gen-card__body span { font-weight: 300; color: var(--text); }
  .gen-card__years { color: #fff; font-weight: 700; font-size: 12.5px; height: 17px; line-height: 17px; text-align: center; }
  .gen-card__art { position: absolute; border-radius: 6px; }

  .gen-card--first { left: 111px; width: 188px; }
  .gen-card--first .gen-card__head, .gen-card--first .gen-card__years { background: var(--green); }
  .gen-card--first .gen-card__body { height: 61px; }
  .gen-card--second { left: 331px; width: 195px; }
  .gen-card--second .gen-card__head, .gen-card--second .gen-card__years { background: var(--crimson); }
  .gen-card--second .gen-card__body { height: 96px; }
  .gen-card--third { left: 556px; width: 196px; }
  .gen-card--third .gen-card__head, .gen-card--third .gen-card__years { background: var(--gold); }
  .gen-card--third .gen-card__body { height: 146px; }

  .timeline { position: absolute; left: 0; top: 0; }
  .milestone { position: absolute; text-align: center; font-size: 18px; line-height: 21px; color: #333; white-space: nowrap; font-weight: 300; }
  .milestone b { font-weight: 700; color: var(--strong); }
  .milestone small { font-size: 7px; font-weight: 400; }
  .milestone .year { display: block; color: var(--blue); font-size: 21px; line-height: 24px; font-weight: 400; }
  .milestone .year small { font-size: 8px; }

  .compare-bar { position: absolute; top: 1190px; height: 10px; }
</style>
</head>
<body>
<div class="canvas">
  <header class="masthead"><h1>Reliability Centred Maintenance (RCM)</h1></header>

  <svg class="side-rail" width="45" height="1004" viewBox="0 0 45 1004" aria-hidden="true">
    <path d="M45 0 L45 1004 L0 1004 L0 80 Q0 60 12 45 Z" fill="var(--ink)"/>
    <path d="M45 456 L45 888 L0 940 L0 520 Q0 500 12 490 Z" fill="var(--blue)"/>
  </svg>

  <h2 class="section-title" style="top:200px">RCM Generations</h2>
  <div class="section-rule" style="top:261px"></div>

  <article class="gen-card gen-card--first">
    <div class="gen-card__head">1st Generation</div>
    <div class="gen-card__body"><span>Fix it When Breaks</span></div>
    <div class="gen-card__years">1930-1950</div>
    <div class="gen-card__art" role="img" aria-label="Steam locomotive" style="left:32px;top:165px;width:128px;height:93px;background:linear-gradient(135deg,#4a4d52,#1e1f22)"></div>
  </article>

  <article class="gen-card gen-card--second">
    <div class="gen-card__head">2nd Generation</div>
    <div class="gen-card__body"><span>Higher Availibility</span><br><b>Lower Cost</b><br><span>Longer Asset life</span></div>
    <div class="gen-card__years">1950-1970</div>
    <div class="gen-card__art" role="img" aria-label="Battle tank" style="left:6px;top:186px;width:180px;height:72px;background:linear-gradient(135deg,#9a9a9a,#2a2a2a)"></div>
  </article>

  <article class="gen-card gen-card--third">
    <div class="gen-card__head">3rd Generation</div>
    <div class="gen-card__body"><span>Higher Availibility</span><br><b>Greater Safety</b><br><span>Better Product Quality</span><br><b>Longer Asset life</b><br><span>Environment Friendly</span><br><b>Cost Effective</b></div>
    <div class="gen-card__years">1970-2000</div>
    <div class="gen-card__art" role="img" aria-label="Jet airliner" style="left:6px;top:250px;width:190px;height:60px;background:linear-gradient(135deg,#f2f2f2,#9aa0a6)"></div>
  </article>

  <h2 class="section-title" style="top:665px">TimeLine</h2>
  <div class="section-rule" style="top:725px"></div>

  <svg class="timeline" width="929" height="1000" viewBox="0 0 929 1000" aria-hidden="true">
    <path d="M146 874 C196 874 200 939 242 939 C284 939 298 876 340 876 C382 876 391 938 433 938 C475 938 485 874 527 874 C569 874 583 939 625 939 C667 939 678 874 720 874 C762 874 772 939 815 939" fill="none" stroke="var(--blue)" stroke-width="3"/>
    <g fill="var(--blue)" stroke="#fff" stroke-width="5">
      <circle cx="242" cy="939" r="12"/>
      <circle cx="340" cy="876" r="12"/>
      <circle cx="433" cy="938" r="12"/>
      <circle cx="527" cy="874" r="12"/>
      <circle cx="625" cy="939" r="12"/>
      <circle cx="720" cy="874" r="12"/>
    </g>
  </svg>

  <div class="milestone" style="left:242px;top:953px;transform:translateX(-50%)"><span class="year">1950</span>Complex machine<br><b>Engine overl haul</b></div>
  <div class="milestone" style="left:340px;top:813px;transform:translateX(-50%)"><b>1st decision</b> diagram<span class="year">1965<small>-&gt;</small>1968</span></div>
  <div class="milestone" style="left:433px;top:955px;transform:translateX(-50%)"><span class="year">1969<small>-&gt;</small>1973</span><b>MSG1</b> developed<br>applied to <b>Aerolux 583</b></div>
  <div class="milestone" style="left:527px;top:789px;transform:translateX(-50%)"><b>MSG2</b> developed<br><small>applied to</small> <b>QX10</b> and <b>Starline</b><span class="year">1970<small>-&gt;</small>1975</span></div>
  <div class="milestone" style="left:625px;top:955px;transform:translateX(-50%)"><span class="year">1976<small>-&gt;</small>1984</span><b>DMA</b> asks reports<br>Maintenance program</div>
  <div class="milestone" style="left:720px;top:792px;transform:translateX(-50%)"><b>Marlow</b> &amp; <b>Kent</b> <small>report</small><br><b>RCM</b><span class="year">1978<small>-&gt;</small>1984</span></div>

  <h2 class="section-title" style="top:1064px">Comparison</h2>
  <div class="section-rule" style="top:1138px"></div>

  <div class="compare-bar" style="left:415px;width:129px;background:var(--maroon)"></div>
  <div class="compare-bar" style="left:544px;width:128px;background:var(--teal)"></div>
</div>
</body>
</html>
```